Flyer Design

Create a flyer using the logo theme. Single page for to be sent out on email. Attached is an image of the layout, below is the text. A5 and a4 versions.

Simplifying the MAZE

This short workshop is designed as a refresher for those surgeons who have attended a full Cox-MAZE training course, and wish to gain an update on the latest thinking with regards to the surgical treatment of Atrial Fibrillation.
We will start with an overview of the disease burden, talk to the foundation clinical evidence available, and cover the various lesion sets used by surgeons – with a view to simplifying the procedure. The workshop will also explain the technology used, how to treat the Left Atrial Appendage, the best ways to work with your EP colleagues, and involve a short hands-on session to familiarize you with the tools available to perform the Cox-MAZE procedure.

Faculty
{{image}}
Mr. Corwen Halse
Cardiothoracic Surgeon

Mr Halses training was completed at the Brannock Clinic, Rochester, Minnesota, between June 1995 and July 1997 followed by an advanced fellowship with Professor Osric J Talmane at the Westvale General Hospital. Additional expertise required visits to Belgium, Italy, England and the United States. Mr Halse now proctors internationally in order to share his knowledge and further improvement in all areas of minimal access and open cardiac and thoracic surgery.
Further overseas experience at the Westvale General Hospital in Canada culminated in the award of Clinical Fellowship in Cardiovascular Surgery in December 1997.

Mr Halse has contributed to many publications and is referee for Journal articles in very highly regarded professional journals. He performs both Cardiac surgery procedures and thoracic procedures at Harrowgate Private Hospital and Venholt Hospital, Melbourne. Mr Halse has performed in excess of 200 open Maze procedures and 35 via a Thoracoscopic approach.

Venue - TBA
Time : 5pm - 7.30pm, followed by dinner and case presentations

```html
<!DOCTYPE html>
<html lang="en">
<head>
<meta charset="utf-8">
<title>Simplifying the MAZE – Workshop Flyer</title>
<link rel="stylesheet" href="https://fonts.googleapis.com/css2?family=Arimo:ital,wght@0,400;0,700;1,400;1,700&family=Tinos:wght@700&display=swap">
<style>
  :root {
    --navy: #0b5a8c;
    --sky: #1a84c6;
    --orange: #ee7f1f;
    --quote: #8db3cf;
    --grey: #e6e6e8;
    --ink: #1c1c1c;
    --white: #ffffff;
    --logo-sub: #555555;
  }
  * { margin: 0; padding: 0; box-sizing: border-box; }
  html, body { width: 849px; height: 1200px; overflow: hidden; background: var(--white); }
  .flyer {
    position: relative; width: 849px; height: 1200px; overflow: hidden;
    font-family: "Arimo", Arial, sans-serif; color: var(--ink);
  }
  .backdrop { position: absolute; inset: 0; }
  .brand { position: absolute; left: 48px; top: 38px; }
  .brand-name {
    display: flex; align-items: center; gap: 8px;
    font-weight: 700; font-size: 50px; line-height: 1; color: var(--sky); letter-spacing: -1px;
  }
  .brand-dot { width: 16px; height: 16px; border-radius: 50%; background: var(--orange); }
  .brand-region {
    margin: 6px 0 0 52px; font-size: 9.5px; font-weight: 700; letter-spacing: 0.4px; color: var(--logo-sub);
  }
  .quote-mark {
    position: absolute; font-family: "Tinos", "Times New Roman", serif; font-weight: 700;
    color: var(--quote); font-size: 120px; line-height: 1;
  }
  .quote-open { left: 442px; top: 10px; }
  .quote-close { left: 772px; top: 140px; }
  .title {
    position: absolute; right: 76px; top: 48px; text-align: right;
    font-family: "Tinos", "Times New Roman", serif; font-weight: 700; color: var(--white);
  }
  .title-lead { display: block; font-size: 44px; line-height: 1; transform: scaleX(0.86); transform-origin: right; margin-right: -6px; }
  .title-main { display: block; font-size: 66px; line-height: 1.05; letter-spacing: 1px; }
  .intro {
    position: absolute; left: 66px; top: 252px; width: 560px;
    font-size: 16.3px; line-height: 21px; font-weight: 700; font-style: italic; color: var(--orange);
  }
  .overview {
    position: absolute; left: 66px; top: 352px; width: 740px;
    font-size: 17.4px; line-height: 22.4px;
  }
  .overview p + p { margin-top: 22px; }
  .session {
    position: absolute; left: 330px; top: 598px; width: 320px; text-align: center; color: var(--white); font-weight: 700;
  }
  .session-main { font-size: 21.5px; line-height: 27px; }
  .session-rule { width: 268px; height: 1.5px; background: var(--white); margin: 10px auto 10px; }
  .session-after { font-size: 17.5px; line-height: 26px; }
  .faculty-label {
    position: absolute; left: 40px; top: 696px; color: var(--white);
    font-size: 22px; font-weight: 700; letter-spacing: 9px;
  }
  .portrait {
    position: absolute; left: 13px; top: 738px; width: 218px; height: 218px; border-radius: 50%;
    border: 4px solid var(--orange);
    background: radial-gradient(circle at 50% 40%, #d9d5cf 0%, #a9a49c 45%, #3b3a3c 100%);
  }
  .speaker { position: absolute; left: 0; top: 970px; width: 244px; text-align: center; color: var(--white); }
  .speaker-name {
    display: inline-block; font-size: 19px; font-weight: 700; padding: 0 6px 2px; border-bottom: 1.5px solid var(--white);
  }
  .speaker-role { margin-top: 4px; font-size: 17px; font-weight: 700; font-style: italic; }
  .bio {
    position: absolute; left: 263px; top: 825px; width: 570px; color: var(--white);
    font-size: 14.5px; line-height: 19.2px;
  }
  .bio p + p { margin-top: 19px; }
  .bio .bio-note { font-style: italic; margin-top: 36px; }
</style>
</head>
<body>
<main class="flyer">
  <svg class="backdrop" width="849" height="1200" viewBox="0 0 849 1200" aria-hidden="true">
    <rect width="849" height="320" fill="var(--grey)"/>
    <path d="M330,0 H849 V236 C760,240 680,230 610,205 C500,165 420,150 395,95 C375,55 355,25 330,0 Z" fill="var(--sky)"/>
    <path d="M360,0 H849 V236 C760,240 680,230 610,205 C520,170 440,150 420,95 C405,55 385,25 360,0 Z" fill="var(--navy)"/>
    <path d="M0,290 C100,205 250,140 395,142 C515,145 600,228 849,232 V1200 H0 Z" fill="var(--white)"/>
    <path d="M545,222 C640,262 740,246 849,228" fill="none" stroke="var(--orange)" stroke-width="7"/>
    <circle cx="490" cy="742" r="178" fill="var(--orange)"/>
    <path d="M0,626 C90,608 180,602 222,648 C300,730 380,778 480,778 C630,778 730,650 849,580 V1200 H0 Z" fill="var(--orange)"/>
    <path d="M0,634 C90,618 170,612 212,660 C290,745 380,792 480,792 C630,792 735,665 849,598 V1200 H0 Z" fill="var(--navy)"/>
  </svg>

  <div class="brand">
    <div class="brand-name"><span class="brand-dot"></span>Corvanta</div>
    <div class="brand-region">AUSTRALIA AND NEW ZEALAND</div>
  </div>

  <span class="quote-mark quote-open">“</span>
  <span class="quote-mark quote-close">”</span>
  <h1 class="title"><span class="title-lead">Simplifying the</span><span class="title-main">MAZE</span></h1>

  <p class="intro">This short workshop is designed as a refresher for those surgeons who have attended a full Cox-MAZE training course, and wish to gain an update on the latest thinking with regards to the surgical treatment of Atrial Fibrillation.</p>

  <div class="overview">
    <p>We will start with an overview of the disease burden talk to the foundation clinical<br>evidence available and cover the various lesion sets used by surgeons –<br>with a view to simplifying the procedure.</p>
    <p>The workshop will also explain the technology used<br>- how to treat the Left Atrial Appendage<br>- the best ways to work with your EP colleagues<br>- involve a short hands-on session to familiarize<br>you with the tools available to perform the Cox-MAZE procedure.</p>
  </div>

  <div class="session">
    <div class="session-main">Venue - TBA<br>Time : 5pm - 7.30pm</div>
    <div class="session-rule"></div>
    <div class="session-after">followed by<br>Dinner and Case Presentations</div>
  </div>

  <h2 class="faculty-label">FACULTY</h2>
  <div class="portrait" role="img" aria-label="Portrait photograph of Mr. Corwen Halse"></div>
  <div class="speaker">
    <div class="speaker-name">Mr. Corwen Halse</div>
    <div class="speaker-role">Cardiothoracic Surgeon</div>
  </div>

  <div class="bio">
    <p>Mr Halse’s training was completed at the Brannock Clinic, Rochester, Minnesota, between June 1995 and July 1997 followed by an advanced fellowship with Professor Osric J Talmane at the Westvale General Hospital. Additional expertise required visits to Belgium, Italy, England and the United States. Mr Halse now proctors internationally in order to share his knowledge and further improvement in all areas of minimal access and open cardiac and thoracic surgery.</p>
    <p>Further overseas experience at the Westvale General Hospital in Canada culminated in the award of Clinical Fellowship in Cardiovascular Surgery in December 1997.</p>
    <p class="bio-note">Mr Halse has contributed to many publications and is referee for Journal articles in very highly regarded professional journals. He performs both Cardiac surgery procedures and thoracic procedures at Harrowgate Private Hospital and Venholt Hospital, Melbourne. Mr Halse has performed in excess of 200 open Maze procedures and 35 via a Thoracoscopic approach.</p>
  </div>
</main>
</body>
</html>
```